依頼詳細
家計簿アプリには以下の機能ボタンがあります。そのボタン用のアイコン制作をお願いします。カッコ内はアイコンのイメージです。
・入力(鉛筆)
・履歴/カレンダー(カレンダー)
・グラフ(円グラフ)
・タグ(タグ)
・クレジットカード(クレジットカード)

適当なアイコンに私が適当に着色したものを添付しています。これを見て頂ければイメージがつくと思います。この添付ファイルのアイコンの中で鉛筆とカレンダー、タグはおおまかにはイメージ通りで、これらを洗練する方向で制作願います。円グラフは真ん中がくり抜かれたドーナツ型のほうが望ましいです。一部を大きくする必要はないです。
クレジットカードはかなり改善の余地ありです。
アイコンの背景色は自由に変更できますので、その点も考慮が必要ですが、添付ファイルの背景色がデフォルトとなりますので、この色に最もマッチするようにお願いします。背景色は基本的にはルミナリカラーの400番代が選択されますので、全体の色調などはそこに合わせて下さい。
提案時にはデフォルト色(42A5F5)、赤系(ef5350)、緑系(9CCC65)、オレンジ系(FFA726)、グレー系(BDBDBD)の各色を背景色としてサンプルをご提示頂けると助かります。

参考:
https://www.hueparlor.co/colors

記載項目
表示サイズは24px x 24pxとなります。
希望イメージ
希望する色
背景色は可変となります。
納品ファイル
• イラストレーター形式 (.ai)
• PNG形式 (.png)
補足説明
SVG形式での納品もお願いします(必須)
1~3回程度手直しをお願いするかもしれませんので、よろしくお願いいたします。
すみません、表示サイズを24px x 24pxとしていましたが、28px x 24pxとして下さい。
よろしくお願いいたします。

```html
<!DOCTYPE html>
<html lang="ja">
<head>
<meta charset="utf-8">
<title>入力</title>
<link href="https://fonts.googleapis.com/css2?family=Noto+Sans+JP:wght@400;500;700&family=Roboto:wght@400;500&display=swap" rel="stylesheet">
<style>
  :root {
    --status: #2f5a48;
    --appbar: #ff9800;
    --toolbar: #ffa726;
    --tool-line: #fff3dc;
    --ink: #212121;
    --ink-soft: #424242;
    --progress: #42a5f5;
    --track: #e0e0e0;
    --nav: #000;
    --white: #fff;
    --bg-blue: #42a5f5; --bg-red: #ef5350; --bg-green: #9ccc65; --bg-orange: #ffa726; --bg-grey: #bdbdbd;
    --c-food: #e53935; --c-eatout: #d81b60; --c-social: #8e24aa; --c-transit: #5e35b1;
    --c-daily: #3949ab; --c-wear: #1e88e5; --c-leisure: #039be5; --c-study: #00acc1;
    --c-home: #00897b; --c-utility: #43a047; --c-insure: #7cb342; --c-tax: #c0ca33;
    --c-big: #fdd835; --c-other: #fb8c00;
  }
  * { margin: 0; padding: 0; box-sizing: border-box; }
  html, body { width: 675px; height: 1200px; overflow: hidden; background: var(--white); }
  body { font-family: "Noto Sans JP", "Roboto", sans-serif; color: var(--ink); position: relative; }
  .icon-defs { position: absolute; width: 0; height: 0; overflow: hidden; }

  .status-bar { position: absolute; top: 0; left: 0; width: 675px; height: 45px; background: var(--status);
    color: var(--white); display: flex; align-items: center; justify-content: space-between; padding: 0 16px; }
  .status-bar .carrier { font-size: 19px; }
  .status-bar .right { display: flex; align-items: center; gap: 12px; font-family: "Roboto", sans-serif; font-size: 23px; }

  .app-bar { position: absolute; top: 45px; left: 0; width: 675px; height: 74px; background: var(--appbar); color: var(--white); }
  .app-bar .menu { position: absolute; left: 18px; top: 20px; }
  .app-bar .title { position: absolute; width: 100%; text-align: center; top: 13px; font-size: 34px; font-weight: 500; }
  .app-bar .book { position: absolute; right: 14px; top: 19px; font-size: 24px; display: flex; align-items: center; gap: 6px; }

  .tool-bar { position: absolute; top: 119px; left: 0; width: 675px; height: 95px; background: var(--toolbar); color: var(--tool-line); }
  .tool-bar svg { position: absolute; top: 24px; }

  .summary { position: absolute; top: 255px; width: 675px; text-align: center; }
  .summary .expense { font-size: 28px; font-weight: 500; display: flex; justify-content: center; align-items: baseline; gap: 14px; }
  .summary .expense .amount { font-size: 48px; font-weight: 700; letter-spacing: 1px; }
  .summary .more { position: absolute; left: 500px; top: 18px; }
  .progress { position: absolute; top: 72px; left: 141px; width: 393px; height: 14px; border-radius: 7px; background: var(--track); overflow: hidden; }
  .progress .fill { width: 64%; height: 100%; background: var(--progress); border-radius: 7px; }
  .summary .balance { position: absolute; top: 94px; width: 100%; font-size: 20px; color: var(--ink-soft); }

  .tabs { position: absolute; top: 390px; left: 74px; width: 527px; display: flex; }
  .tabs .tab { flex: 1; text-align: center; font-size: 32px; padding-bottom: 14px; border-bottom: 8px solid var(--track); color: var(--ink-soft); }
  .tabs .tab.active { border-bottom-color: #555; color: var(--ink); font-weight: 700; }

  .categories { position: absolute; top: 480px; left: 62px; width: 600px; display: grid; grid-template-columns: repeat(4, 167px); row-gap: 20px; }
  .category { display: flex; flex-direction: column; align-items: center; width: 92px; }
  .category .label { margin-top: 8px; font-size: 21px; white-space: nowrap; }

  .swatches { position: absolute; top: 1048px; left: 14px; width: 647px; display: flex; gap: 8px; }
  .swatch { flex: 1; height: 58px; border-radius: 6px; display: flex; align-items: center; justify-content: center; gap: 3px; color: var(--white); }
  .swatch.blue { background: var(--bg-blue); }
  .swatch.red { background: var(--bg-red); }
  .swatch.green { background: var(--bg-green); }
  .swatch.orange { background: var(--bg-orange); }
  .swatch.grey { background: var(--bg-grey); }

  .nav-bar { position: absolute; bottom: 0; left: 0; width: 675px; height: 75px; background: var(--nav); }
  .nav-bar svg { position: absolute; top: 20px; }
</style>
</head>
<body>
  <svg class="icon-defs" aria-hidden="true">
    <symbol id="i-pencil" viewBox="0 0 24 24"><g fill="none" stroke="currentColor" stroke-width="1.6" stroke-linejoin="round"><path d="M4 20l1-5L16 4l4 4L9 19z"/><path d="M13.5 6.5l4 4"/></g></symbol>
    <symbol id="i-calendar" viewBox="0 0 24 24"><g fill="none" stroke="currentColor" stroke-width="1.6"><rect x="3" y="5" width="18" height="16" rx="1.5"/><path d="M3 10h18M8 3v4M16 3v4"/><path d="M7 13h2M11 13h2M15 13h2M7 17h2M11 17h2" stroke-width="1.4"/></g></symbol>
    <symbol id="i-donut" viewBox="0 0 24 24"><g fill="none" stroke="currentColor" stroke-width="1.6"><circle cx="12" cy="12" r="9"/><circle cx="12" cy="12" r="3.5"/><path d="M12 3v5.5M15 13l6 3"/></g></symbol>
    <symbol id="i-tag" viewBox="0 0 24 24"><path d="M12 3h8v8l-9 9-8-8z M16.5 6a1.5 1.5 0 1 0 0.01 0z" fill="currentColor" fill-rule="evenodd"/></symbol>
    <symbol id="i-card" viewBox="0 0 24 24"><g fill="none" stroke="currentColor" stroke-width="1.6"><rect x="2.5" y="5" width="19" height="14" rx="2"/><path d="M2.5 9.5h19M5.5 15h5"/></g></symbol>
  </svg>

  <div class="status-bar">
    <span class="carrier">SIMがありま…</span>
    <span class="right">
      <svg width="22" height="22" viewBox="0 0 22 22" fill="none" stroke="#fff" stroke-width="2"><path d="M6 15V10a5 5 0 0 1 10 0v5l2 2H4z"/><path d="M3 3l16 16"/></svg>
      <svg width="24" height="14" viewBox="0 0 24 14" fill="none" stroke="#fff" stroke-width="2"><rect x="1" y="1" width="20" height="12" rx="1"/></svg>
      <span>15:54</span>
    </span>
  </div>

  <header class="app-bar">
    <svg class="menu" width="40" height="34" viewBox="0 0 40 34"><g fill="#fff"><rect y="2" width="40" height="5" rx="2"/><rect y="14" width="40" height="5" rx="2"/><rect y="26" width="40" height="5" rx="2"/></g></svg>
    <div class="title">入力</div>
    <div class="book">家計 <svg width="16" height="26" viewBox="0 0 16 26"><path d="M3 3l10 10-10 10" fill="none" stroke="#fff" stroke-width="3.5"/></svg></div>
  </header>

  <nav class="tool-bar">
    <svg style="left:58px" width="46" height="46"><use href="#i-pencil"/></svg>
    <svg style="left:184px" width="46" height="46"><use href="#i-calendar"/></svg>
    <svg style="left:315px" width="46" height="46"><use href="#i-donut"/></svg>
    <svg style="left:440px" width="46" height="46"><use href="#i-tag"/></svg>
    <svg style="left:571px" width="46" height="46"><use href="#i-card"/></svg>
  </nav>

  <section class="summary">
    <div class="expense"><span>支出</span><span class="amount">¥125,000</span></div>
    <svg class="more" width="8" height="30" viewBox="0 0 8 30" fill="#757575"><circle cx="4" cy="4" r="3"/><circle cx="4" cy="15" r="3"/><circle cx="4" cy="26" r="3"/></svg>
    <div class="progress"><div class="fill"></div></div>
    <div class="balance">収支 ¥75,000</div>
  </section>

  <div class="tabs">
    <div class="tab">収入</div>
    <div class="tab active">支出</div>
  </div>

  <main class="categories">
    <div class="category"><svg width="80" height="80" viewBox="0 0 80 80"><circle cx="40" cy="40" r="38" fill="var(--c-food)"/><g stroke="#fff" stroke-width="3" fill="none" stroke-linecap="round"><path d="M30 22v12a4 4 0 0 0 8 0V22M34 22v36"/><path d="M48 58V22c5 2 6 10 6 16h-6"/></g></svg><span class="label">食費</span></div>
    <div class="category"><svg width="80" height="80" viewBox="0 0 80 80"><circle cx="40" cy="40" r="38" fill="var(--c-eatout)"/><g stroke="#fff" stroke-width="3" fill="none"><path d="M24 38h32l-4 18H28z"/><path d="M32 38V20M40 38V20M48 38V20"/></g></svg><span class="label">外食</span></div>
    <div class="category"><svg width="80" height="80" viewBox="0 0 80 80"><circle cx="40" cy="40" r="38" fill="var(--c-social)"/><g stroke="#fff" stroke-width="3" fill="none"><rect x="26" y="26" width="22" height="30" rx="2"/><path d="M48 32h5a3 3 0 0 1 3 3v8a3 3 0 0 1-3 3h-5"/><path d="M24 26c0-6 26-6 26 0" fill="#fff"/></g></svg><span class="label">交際</span></div>
    <div class="category"><svg width="80" height="80" viewBox="0 0 80 80"><circle cx="40" cy="40" r="38" fill="var(--c-transit)"/><g stroke="#fff" stroke-width="3" fill="none"><rect x="26" y="20" width="28" height="32" rx="6"/><path d="M26 36h28M32 52l-5 7M48 52l5 7"/><circle cx="33" cy="45" r="1.5" fill="#fff"/><circle cx="47" cy="45" r="1.5" fill="#fff"/></g></svg><span class="label">交通</span></div>

    <div class="category"><svg width="80" height="80" viewBox="0 0 80 80"><circle cx="40" cy="40" r="38" fill="var(--c-daily)"/><g stroke="#fff" stroke-width="3.5" fill="none" stroke-linecap="round"><path d="M26 56l22-22"/><path d="M46 28l8 8M50 24l8 8"/></g></svg><span class="label">日用品</span></div>
    <div class="category"><svg width="80" height="80" viewBox="0 0 80 80"><circle cx="40" cy="40" r="38" fill="var(--c-wear)"/><path d="M32 22l-12 8 5 8 5-3v21h20V35l5 3 5-8-12-8c-2 4-14 4-16 0z" fill="#fff"/></svg><span class="label">服・美容</span></div>
    <div class="category"><svg width="80" height="80" viewBox="0 0 80 80"><circle cx="40" cy="40" r="38" fill="var(--c-leisure)"/><g stroke="#fff" stroke-width="2.5" fill="none"><circle cx="40" cy="32" r="6"/><path d="M40 20v-4M28 32h-4M56 32h-4M31 23l-3-3M49 23l3-3"/><path d="M24 52h32l-4-8H28z"/></g></svg><span class="label">レジャー</span></div>
    <div class="category"><svg width="80" height="80" viewBox="0 0 80 80"><circle cx="40" cy="40" r="38" fill="var(--c-study)"/><g stroke="#fff" stroke-width="3" fill="none" stroke-linejoin="round"><path d="M25 55l2-9 22-22 7 7-22 22z"/><path d="M44 29l7 7"/></g></svg><span class="label">教育・教養</span></div>

    <div class="category"><svg width="80" height="80" viewBox="0 0 80 80"><circle cx="40" cy="40" r="38" fill="var(--c-home)"/><g stroke="#fff" stroke-width="3" fill="none" stroke-linejoin="round"><path d="M22 40l18-16 18 16M27 36v20h26V36"/><rect x="36" y="44" width="8" height="12"/></g></svg><span class="label">住居</span></div>
    <div class="category"><svg width="80" height="80" viewBox="0 0 80 80"><circle cx="40" cy="40" r="38" fill="var(--c-utility)"/><g fill="#fff"><path d="M36 22l14-4v30h-3V26l-11 3v24h-3z"/><ellipse cx="31" cy="53" rx="6" ry="4.5"/><ellipse cx="45" cy="49" rx="6" ry="4.5"/></g></svg><span class="label">水道光熱</span></div>
    <div class="category"><svg width="80" height="80" viewBox="0 0 80 80"><circle cx="40" cy="40" r="38" fill="var(--c-insure)"/><g stroke="#fff" stroke-width="3" fill="none"><rect x="20" y="31" width="40" height="18" rx="9" transform="rotate(-40 40 40)"/><path d="M34 33l12 14"/></g></svg><span class="label">保険</span></div>
    <div class="category"><svg width="80" height="80" viewBox="0 0 80 80"><circle cx="40" cy="40" r="38" fill="var(--c-tax)"/><g stroke="#fff" stroke-width="3" fill="none"><path d="M27 28h26l-3 28H30z"/><rect x="25" y="22" width="30" height="6" rx="1"/></g></svg><span class="label">税金</span></div>

    <div class="category"><svg width="80" height="80" viewBox="0 0 80 80"><circle cx="40" cy="40" r="38" fill="var(--c-big)"/><g stroke="#fff" stroke-width="3" fill="none" stroke-linejoin="round"><rect x="26" y="28" width="28" height="14" rx="3"/><path d="M22 40h36v10H22zM26 50v5M54 50v5"/></g></svg><span class="label">大型出費</span></div>
    <div class="category"><svg width="80" height="80" viewBox="0 0 80 80"><circle cx="40" cy="40" r="38" fill="var(--c-other)"/><g stroke="#fff" stroke-width="3" fill="none"><path d="M30 40a12 12 0 1 1 20 0c-2 3-5 4-10 4s-8-1-10-4z"/><path d="M36 44l-2 12h12l-2-12"/></g></svg><span class="label">その他</span></div>
  </main>

  <section class="swatches" aria-label="背景色サンプル">
    <div class="swatch blue"><svg width="20" height="20"><use href="#i-pencil"/></svg><svg width="20" height="20"><use href="#i-calendar"/></svg><svg width="20" height="20"><use href="#i-donut"/></svg><svg width="20" height="20"><use href="#i-tag"/></svg><svg width="20" height="20"><use href="#i-card"/></svg></div>
    <div class="swatch red"><svg width="20" height="20"><use href="#i-pencil"/></svg><svg width="20" height="20"><use href="#i-calendar"/></svg><svg width="20" height="20"><use href="#i-donut"/></svg><svg width="20" height="20"><use href="#i-tag"/></svg><svg width="20" height="20"><use href="#i-card"/></svg></div>
    <div class="swatch green"><svg width="20" height="20"><use href="#i-pencil"/></svg><svg width="20" height="20"><use href="#i-calendar"/></svg><svg width="20" height="20"><use href="#i-donut"/></svg><svg width="20" height="20"><use href="#i-tag"/></svg><svg width="20" height="20"><use href="#i-card"/></svg></div>
    <div class="swatch orange"><svg width="20" height="20"><use href="#i-pencil"/></svg><svg width="20" height="20"><use href="#i-calendar"/></svg><svg width="20" height="20"><use href="#i-donut"/></svg><svg width="20" height="20"><use href="#i-tag"/></svg><svg width="20" height="20"><use href="#i-card"/></svg></div>
    <div class="swatch grey"><svg width="20" height="20"><use href="#i-pencil"/></svg><svg width="20" height="20"><use href="#i-calendar"/></svg><svg width="20" height="20"><use href="#i-donut"/></svg><svg width="20" height="20"><use href="#i-tag"/></svg><svg width="20" height="20"><use href="#i-card"/></svg></div>
  </section>

  <footer class="nav-bar">
    <svg style="left:172px" width="32" height="34" viewBox="0 0 32 34"><path d="M28 3L4 17l24 14z" fill="none" stroke="#fff" stroke-width="3" stroke-linejoin="round"/></svg>
    <svg style="left:321px" width="34" height="34" viewBox="0 0 34 34"><circle cx="17" cy="17" r="14" fill="none" stroke="#fff" stroke-width="3"/></svg>
    <svg style="left:472px" width="32" height="34" viewBox="0 0 32 34"><rect x="3" y="4" width="26" height="26" rx="2" fill="none" stroke="#fff" stroke-width="3"/></svg>
  </footer>
</body>
</html>
```